Engineering Consultant Business Card

I'm starting a new business as a high-end engineering consultant in a niche field. I've attached the jpg for my logo plus the branding guideline document that I've been following. You can see my business website here: www.tarvikworks.com
I'd like a business card that has the logo on one side, then the other side has (in any order): Tarvik Works, Inc.
Dana Whitlock
President and Chief EMC Engineer
www.tarvikworks.com
dana@tarvikworks.com
Optional: motto "We will solve your EMC problems as early as possible—ideally before they even start."
I'm not planning on including a phone number
Target Market(s)
Businesses, especially makers of electronics hardware
Industry/Entity Type
Electrical engineering
Contact Information for Business Card
Company name, my name, website, email

```html
<!DOCTYPE html>
<html lang="en">
<head>
<meta charset="utf-8">
<title>Tarvik Works – Business Card</title>
<link rel="stylesheet" href="https://fonts.googleapis.com/css2?family=Open+Sans:wght@400;600;700&display=swap">
<style>
  :root {
    --backdrop: #3b3b3b;
    --card: #141414;
    --brand-blue: #2e4aa6;
    --text-light: #e6e6e6;
    --divider: #2e4aa6;
  }
  * { box-sizing: border-box; margin: 0; padding: 0; }
  html, body {
    width: 1200px; height: 801px; overflow: hidden;
    background: var(--backdrop);
    font-family: "Open Sans", Arial, sans-serif;
  }
  .stage {
    width: 1200px; height: 801px;
    display: flex; align-items: center; justify-content: center; gap: 50px;
  }
  .card {
    width: 525px; height: 300px;
    background: var(--card);
    border-bottom: 2px solid var(--brand-blue);
    border-left: 2px solid var(--brand-blue);
    position: relative;
  }
  .card-front .identity {
    position: absolute; top: 78px; left: 0; right: 0;
    display: flex; justify-content: center; align-items: center;
  }
  .person { text-align: right; padding-right: 22px; }
  .person-name {
    color: var(--brand-blue); font-weight: 700; font-size: 21px;
    letter-spacing: 0.5px; text-transform: uppercase; line-height: 1.2;
  }
  .person-title { color: var(--text-light); font-size: 15px; margin-top: 2px; }
  .divider { width: 1px; height: 78px; background: var(--divider); }
  .contact { padding-left: 22px; color: var(--text-light); font-size: 14px; line-height: 1.5; }
  .company-name { font-weight: 600; font-size: 15px; margin-bottom: 4px; }
  .contact-line { display: flex; align-items: center; gap: 8px; }
  .contact-line svg { width: 12px; height: 12px; flex: none; }
  .motto {
    position: absolute; left: 0; right: 0; top: 196px;
    text-align: center; color: var(--text-light); font-size: 14.5px; line-height: 1.45;
  }
  .card-back { display: flex; align-items: center; justify-content: center; }
  .brand-mark { display: flex; align-items: center; gap: 14px; }
  .brand-dot { width: 30px; height: 30px; border-radius: 50%; background: var(--brand-blue); }
  .brand-name { color: var(--brand-blue); font-weight: 700; font-size: 38px; }
</style>
</head>
<body>
  <main class="stage">
    <section class="card card-front">
      <div class="identity">
        <div class="person">
          <p class="person-name">Dana Whitlock</p>
          <p class="person-title">President and Chief EMC Engineer</p>
        </div>
        <div class="divider"></div>
        <div class="contact">
          <p class="company-name">Tarvik Works, Inc.</p>
          <p class="contact-line">
            <svg viewBox="0 0 12 12" aria-hidden="true"><rect x="0.5" y="2" width="11" height="8" fill="var(--brand-blue)"/><path d="M0.5 2 L6 6.5 L11.5 2" stroke="#141414" stroke-width="1.2" fill="none"/></svg>
            dana@tarvikworks.com
          </p>
          <p class="contact-line">
            <svg viewBox="0 0 12 12" aria-hidden="true"><circle cx="6" cy="6" r="5.5" fill="var(--brand-blue)"/><path d="M0.5 6 H11.5 M6 0.5 C3 3 3 9 6 11.5 M6 0.5 C9 3 9 9 6 11.5" stroke="#141414" stroke-width="0.9" fill="none"/></svg>
            www.tarvikworks.com
          </p>
        </div>
      </div>
      <p class="motto">We will solve your EMC problems as early as possible—<br>ideally before they even start.</p>
    </section>
    <section class="card card-back">
      <div class="brand-mark">
        <span class="brand-dot"></span>
        <span class="brand-name">Tarvik Works</span>
      </div>
    </section>
  </main>
</body>
</html>
```